International Career Development Workshop

I need a Powerpoint revised and designed in a more professional manner for a presentation I will be giving. We are an International Education Company that provides students with Internships Abroad, and are expanding our career development programming to offer more guidance through on-site workshops. I am happy to send along our website to showcase the colors and fonts we use, but we tend to use royal blue, lime green, and white in our color scheme. The final design should communicate opportunity and self-awareness within college students.

Target Market(s)

College Students, University Partners, and International Education Community

Industry/Entity Type

Education

Font styles to use
Sans Serif

Colors
9bcb3b
0355a3
ffffff

Requirements
Must have
• Our logo, our color scheme, a unified, professional theme throughout, Watermark of our logo, thematic sections spread across four sections.
Nice to have
• Videos and graphics
Should not have
• Spelling Errors, sloppy design

```html
<!DOCTYPE html>
<html lang="en">
<head>
<meta charset="UTF-8">
<title>Section Title</title>
<link href="https://fonts.googleapis.com/css2?family=Lato:wght@300;700;900&display=swap" rel="stylesheet">
<style>
  :root {
    --royal-blue: #0d5499;
    --lime: #b3d30c;
    --white: #ffffff;
  }
  * { margin: 0; padding: 0; box-sizing: border-box; }
  html, body {
    width: 1200px;
    height: 900px;
    overflow: hidden;
    background: var(--royal-blue);
  }
  .slide {
    position: relative;
    width: 1200px;
    height: 900px;
    background: var(--royal-blue);
    font-family: "Lato", Arial, sans-serif;
  }
  .section-heading {
    position: absolute;
    left: 177px;
    top: 375px;
    width: 843px;
    text-align: center;
  }
  .section-title {
    color: var(--white);
    font-weight: 700;
    font-size: 80px;
    line-height: 1;
    letter-spacing: 0.5px;
    white-space: nowrap;
  }
  .section-subtext {
    margin-top: 28px;
    border-top: 3px solid var(--lime);
    border-bottom: 3px solid var(--lime);
    padding: 14px 0 15px;
    color: var(--lime);
    font-weight: 300;
    font-size: 22px;
    line-height: 26px;
  }
  .footer-band {
    position: absolute;
    left: 0;
    bottom: 0;
    width: 1200px;
    height: 30px;
    background: var(--lime);
  }
</style>
</head>
<body>
  <main class="slide">
    <div class="section-heading">
      <h1 class="section-title">SECTION TITLE HERE</h1>
      <p class="section-subtext">Subtext here Subtext here Subtext here Subtext here</p>
    </div>
    <div class="footer-band"></div>
  </main>
</body>
</html>
```